Anzeigengestaltung für Unternehmensberatung für Pflegedienste
Zielgruppe
Wir sind eine Unternehmensberatung für Pflegedienste. Es soll eine Werbeanzeige erstellt werden, mit welcher schlecht laufende Pflegedienste, die gerade in einer Krise stecken angesprochen werden,
Der slogan soll einfach klingen : Pflege neu gedaxht: wirtschaftlich, nachhaltig, zukunftssicher
Anzeige in 3 Formaten
1. Format 55.3 mm x 118 mm
2. Format 1/ halbe Seite Quer 176 x 118 mm un
3. Format d 1 x A4 _Seite
Der Name der Firma Keltor GmbH info at keltor.de Tel 0381 72958143 aus Rostock Berlin und bundesweit tätig
Aufgabenstellung
Kreativ und elegant

```html
<!DOCTYPE html>
<html lang="de">
<head>
<meta charset="utf-8">
<title>Keltor – Anzeigen in drei Formaten</title>
<link href="https://fonts.googleapis.com/css2?family=Playfair+Display:wght@700&family=Barlow:wght@600&display=swap" rel="stylesheet">
<style>
  :root{
    --navy:#1f2a4f;
    --orange:#ff7205;
    --white:#ffffff;
    --logo:#9aa6bf;
    --photo-a:#e6c9b4;
    --photo-b:#c99a84;
    --photo-c:#8a5f4c;
    --photo-d:#5a4446;
    --canvas:#ffffff;
  }
  *{margin:0;padding:0;box-sizing:border-box}
  html,body{width:1200px;height:885px;overflow:hidden;background:var(--canvas)}
  .canvas{position:relative;width:1200px;height:885px}
  .ad{position:absolute;background:var(--navy);overflow:hidden;color:var(--white)}
  .ad-photo{position:absolute;
    background:
      radial-gradient(ellipse at 55% 55%, var(--photo-c) 0%, transparent 55%),
      radial-gradient(ellipse at 30% 20%, var(--photo-b) 0%, transparent 60%),
      linear-gradient(135deg, var(--photo-b) 0%, var(--photo-a) 45%, var(--photo-c) 75%, var(--photo-d) 100%);}
  .ad-fade{position:absolute;left:0;right:0;background:linear-gradient(to bottom, rgba(31,42,79,0) 0%, rgba(31,42,79,.55) 45%, var(--navy) 100%)}
  .brand{position:absolute;font-family:'Playfair Display',serif;font-weight:700;color:var(--logo);letter-spacing:.04em;line-height:1}
  .headline{position:absolute;font-family:'Playfair Display',serif;font-weight:700;color:var(--white)}
  .rule{position:absolute;background:var(--white)}
  .lead{position:absolute;font-family:'Barlow',sans-serif;font-weight:600;color:var(--white);white-space:nowrap}
  .contact-bar{position:absolute;left:0;right:0;bottom:0;background:var(--orange);font-family:'Barlow',sans-serif;font-weight:600;color:var(--white)}
  .contact{position:absolute;display:flex;align-items:center;white-space:nowrap;line-height:1}
  .contact svg{fill:var(--white);flex:none}

  /* A4 */
  .ad-a4{left:20px;top:15px;width:604px;height:853px}
  .ad-a4 .ad-photo{left:190px;top:0;width:414px;height:722px}
  .ad-a4 .ad-fade{top:420px;height:302px}
  .ad-a4 .brand{left:28px;top:62px;font-size:34px}
  .ad-a4 .headline{left:28px;top:305px;font-size:56px;line-height:60px}
  .ad-a4 .rule{left:28px;top:572px;width:296px;height:3px}
  .ad-a4 .lead{left:28px;top:608px;font-size:21px;line-height:32px}
  .ad-a4 .contact-bar{height:131px}
  .ad-a4 .contact{font-size:23px;gap:8px}
  .ad-a4 .contact svg{width:20px;height:20px}

  /* Small column */
  .ad-small{left:832px;top:24px;width:159px;height:339px}
  .ad-small .ad-photo{left:38px;top:47px;width:121px;height:226px}
  .ad-small .ad-fade{top:150px;height:123px}
  .ad-small .brand{left:25px;top:12px;font-size:22px}
  .ad-small .headline{left:11px;top:162px;font-size:13px;line-height:16px}
  .ad-small .rule{left:11px;top:232px;width:79px;height:2px}
  .ad-small .lead{left:11px;top:243px;font-size:5.4px;line-height:8.5px}
  .ad-small .contact-bar{height:66px}
  .ad-small .contact{font-size:7.5px;gap:3px}
  .ad-small .contact svg{width:6px;height:6px}

  /* Landscape half page */
  .ad-wide{left:659px;top:426px;width:506px;height:339px}
  .ad-wide .ad-photo{left:279px;top:0;width:227px;height:308px}
  .ad-wide .ad-fade{top:180px;height:128px}
  .ad-wide .brand{left:30px;top:24px;font-size:20px}
  .ad-wide .headline{left:30px;top:62px;font-size:33px;line-height:38px}
  .ad-wide .rule{left:30px;top:235px;width:190px;height:2px}
  .ad-wide .lead{left:30px;top:255px;font-size:14px;line-height:21px}
  .ad-wide .contact-bar{height:31px}
  .ad-wide .contact{font-size:10.5px;gap:3px;top:10px}
  .ad-wide .contact svg{width:8px;height:8px}
</style>
</head>
<body>
<svg width="0" height="0" style="position:absolute" aria-hidden="true">
  <symbol id="icon-mail" viewBox="0 0 24 24"><path d="M2 5h20v14H2z M2 5l10 8 10-8" /><path d="M2 6.5l10 7.5 10-7.5V5H2z" fill="#1f2a4f" opacity="0"/></symbol>
  <symbol id="icon-phone" viewBox="0 0 24 24"><path d="M6.6 10.8a15.1 15.1 0 0 0 6.6 6.6l2.2-2.2a1 1 0 0 1 1-.25 11.4 11.4 0 0 0 3.6.57 1 1 0 0 1 1 1V20a1 1 0 0 1-1 1A17 17 0 0 1 3 4a1 1 0 0 1 1-1h3.5a1 1 0 0 1 1 1c0 1.25.2 2.45.57 3.57a1 1 0 0 1-.25 1z"/></symbol>
  <symbol id="icon-pin" viewBox="0 0 24 24"><path d="M12 2a7 7 0 0 0-7 7c0 5.2 7 13 7 13s7-7.8 7-13a7 7 0 0 0-7-7zm0 9.5A2.5 2.5 0 1 1 12 6.5a2.5 2.5 0 0 1 0 5z"/></symbol>
</svg>

<main class="canvas">

  <!-- A4 -->
  <section class="ad ad-a4">
    <div class="ad-photo" role="img" aria-label="Foto: zwei ältere Hände halten sich gegenseitig fest, warme Pastelltöne"></div>
    <div class="ad-fade"></div>
    <div class="brand">KELTOR</div>
    <h1 class="headline">Pflege neu gedaxht:<br>wirtschaflich,<br>nachhaltig,<br>zukunfssicher</h1>
    <div class="rule"></div>
    <p class="lead">Ist Ihr Pflegedienst in einer Krise?<br>Wir bieten Lösungen für eine nachhaltige Zukunft</p>
    <div class="contact-bar">
      <span class="contact" style="left:62px;top:26px"><svg viewBox="0 0 24 24"><use href="#icon-mail"/></svg>info@keltor.de</span>
      <span class="contact" style="left:362px;top:26px"><svg viewBox="0 0 24 24"><use href="#icon-phone"/></svg>0381 72958143</span>
      <span class="contact" style="left:28px;top:81px"><svg viewBox="0 0 24 24"><use href="#icon-pin"/></svg>Rostock</span>
      <span class="contact" style="left:193px;top:81px"><svg viewBox="0 0 24 24"><use href="#icon-pin"/></svg>Berlin</span>
      <span class="contact" style="left:329px;top:81px"><svg viewBox="0 0 24 24"><use href="#icon-pin"/></svg>und bundesweit tätig</span>
    </div>
  </section>

  <!-- 55 x 118 mm -->
  <section class="ad ad-small">
    <div class="ad-photo" role="img" aria-label="Foto: zwei ältere Hände halten sich gegenseitig fest"></div>
    <div class="ad-fade"></div>
    <div class="brand">KELTOR</div>
    <h2 class="headline">Pflege neu gedaxht:<br>wirtschaflich,<br>nachhaltig,<br>zukunfssicher</h2>
    <div class="rule"></div>
    <p class="lead">Ist Ihr Pflegedienst in einer Krise?<br>Wir bieten Lösungen für eine nachhaltige Zukunft</p>
    <div class="contact-bar">
      <span class="contact" style="left:12px;top:13px"><svg viewBox="0 0 24 24"><use href="#icon-mail"/></svg>info@keltor.de</span>
      <span class="contact" style="left:88px;top:13px"><svg viewBox="0 0 24 24"><use href="#icon-phone"/></svg>0381 72958143</span>
      <span class="contact" style="left:12px;top:31px"><svg viewBox="0 0 24 24"><use href="#icon-pin"/></svg>Rostock</span>
      <span class="contact" style="left:67px;top:31px"><svg viewBox="0 0 24 24"><use href="#icon-pin"/></svg>Berlin</span>
      <span class="contact" style="left:12px;top:49px"><svg viewBox="0 0 24 24"><use href="#icon-pin"/></svg>und bundesweit tätig</span>
    </div>
  </section>

  <!-- Halbe Seite quer -->
  <section class="ad ad-wide">
    <div class="ad-photo" role="img" aria-label="Foto: zwei ältere Hände halten sich gegenseitig fest, warme Pastelltöne"></div>
    <div class="ad-fade"></div>
    <div class="brand">KELTOR</div>
    <h2 class="headline">Pflege neu gedaxht:<br>wirtschaflich,<br>nachhaltig,<br>zukunfssicher</h2>
    <div class="rule"></div>
    <p class="lead">Ist Ihr Pflegedienst in einer Krise?<br>Wir bieten Lösungen für eine nachhaltige Zukunft</p>
    <div class="contact-bar">
      <span class="contact" style="left:29px"><svg viewBox="0 0 24 24"><use href="#icon-mail"/></svg>info@keltor.de</span>
      <span class="contact" style="left:126px"><svg viewBox="0 0 24 24"><use href="#icon-phone"/></svg>0381 72958143</span>
      <span class="contact" style="left:236px"><svg viewBox="0 0 24 24"><use href="#icon-pin"/></svg>Rostock</span>
      <span class="contact" style="left:313px"><svg viewBox="0 0 24 24"><use href="#icon-pin"/></svg>Berlin</span>
      <span class="contact" style="left:376px"><svg viewBox="0 0 24 24"><use href="#icon-pin"/></svg>und bundesweit tätig</span>
    </div>
  </section>

</main>
</body>
</html>
```